Verdant Loop Advisors, LLC

I am looking for a simple, clear layout with my logo prominent and embossed, on the best quality card stock available. I would like the business name and phone number included on the card as well......I dont want my name anywhere on the card and I would like my logo embossed on the card......something simple with a white back......open to designs as long as they go along with recycling symbols and green type stuff.....The address, website, cell number, fax number, and email are listed below

5374 Tillbury Fenwood Road
Fernhollow, MD 20799

c. 240.555.0143 f. 240.555.0187
e. sales@verdantloopadvisors.example
w. www.verdantloopadvisors.example

Industry/Entity Type

Recycling

```html
<!DOCTYPE html>
<html lang="en">
<head>
<meta charset="utf-8">
<title>Verdant Loop Advisors, LLC – Business Card</title>
<link rel="stylesheet" href="https://fonts.googleapis.com/css2?family=Archivo:wght@800&family=Arimo:wght@400&display=swap">
<style>
  :root {
    --backdrop: #e4e6e5;
    --card: #ffffff;
    --green-deep: #237a33;
    --green-bright: #3aa64b;
    --green-soft: #a9d6b5;
    --ink-dark: #2a2a2a;
    --ink-text: #454545;
  }
  * { margin: 0; padding: 0; box-sizing: border-box; }
  html, body {
    width: 1200px; height: 1000px; overflow: hidden;
    background: var(--backdrop);
  }
  .business-card {
    position: absolute; left: 75px; top: 200px;
    width: 1050px; height: 600px;
    background: var(--card);
    overflow: hidden;
    box-shadow: 0 6px 24px rgba(0,0,0,0.12);
  }
  .card-shapes { position: absolute; inset: 0; }
  .brand {
    position: absolute; left: 410px; top: 128px;
    font-family: "Archivo", sans-serif; font-weight: 800;
    color: var(--ink-dark); line-height: 1;
  }
  .brand-name { font-size: 60px; letter-spacing: 1px; }
  .brand-sub { font-size: 22px; letter-spacing: 13px; margin-top: 8px; }
  .contact-list {
    position: absolute; left: 420px; top: 262px; list-style: none;
    font-family: "Arimo", sans-serif; font-size: 29px; color: var(--ink-text);
  }
  .contact-list li { display: flex; align-items: center; height: 40px; white-space: nowrap; }
  .contact-icon { width: 24px; height: 24px; margin-right: 10px; flex: none; }
  .address {
    position: absolute; left: 420px; top: 448px; display: flex;
    font-family: "Arimo", sans-serif; font-size: 29px; color: var(--ink-text);
    line-height: 40px; font-style: normal; white-space: nowrap;
  }
  .address .pin { width: 22px; height: 30px; margin: 5px 8px 0 0; flex: none; }
</style>
</head>
<body>
<div class="business-card">
  <svg class="card-shapes" viewBox="0 0 1050 600" aria-hidden="true">
    <defs>
      <linearGradient id="bandGradient" x1="0" y1="0" x2="0" y2="1">
        <stop offset="0" stop-color="var(--green-deep)"/>
        <stop offset="1" stop-color="var(--green-bright)"/>
      </linearGradient>
    </defs>
    <path class="side-band" d="M120,0 L265,0 C285,210 330,420 405,600 L255,600 C195,420 150,210 120,0 Z" fill="url(#bandGradient)"/>
    <circle class="brand-dot" cx="255" cy="300" r="58" fill="var(--card)"/>
    <path class="corner-leaf" d="M690,0 L1050,0 L1050,335 C900,310 750,180 690,0 Z" fill="var(--green-soft)"/>
    <path class="corner-arrow" d="M790,45 L905,45 L905,20 L958,62 L905,104 L905,79 L825,79 Z" fill="var(--card)"/>
  </svg>

  <div class="brand">
    <div class="brand-name">VERDANT LOOP</div>
    <div class="brand-sub">ADVISORS, LLC</div>
  </div>

  <ul class="contact-list">
    <li><svg class="contact-icon" viewBox="0 0 24 24"><circle cx="12" cy="12" r="12" fill="var(--green-bright)"/><rect x="8" y="5" width="8" height="14" rx="1.5" fill="#fff"/></svg>240.555.0143</li>
    <li><svg class="contact-icon" viewBox="0 0 24 24"><circle cx="12" cy="12" r="12" fill="var(--green-bright)"/><rect x="6" y="9" width="12" height="8" rx="1" fill="#fff"/><rect x="8" y="5" width="8" height="4" fill="#fff"/></svg>240.555.0187</li>
    <li><svg class="contact-icon" viewBox="0 0 24 24"><circle cx="12" cy="12" r="12" fill="var(--green-bright)"/><rect x="6" y="8" width="12" height="8" fill="#fff"/><path d="M6,8 L12,13 L18,8" fill="none" stroke="var(--green-bright)" stroke-width="1.5"/></svg>sales@verdantloopadvisors.example</li>
    <li><svg class="contact-icon" viewBox="0 0 24 24"><circle cx="12" cy="12" r="12" fill="var(--green-bright)"/><circle cx="12" cy="12" r="6.5" fill="none" stroke="#fff" stroke-width="1.5"/><path d="M5.5,12 H18.5 M12,5.5 V18.5" stroke="#fff" stroke-width="1.5"/></svg>www.verdantloopadvisors.example</li>
  </ul>

  <address class="address">
    <svg class="pin" viewBox="0 0 22 30"><path d="M11,0 C4.9,0 0,4.9 0,11 C0,19 11,30 11,30 C11,30 22,19 22,11 C22,4.9 17.1,0 11,0 Z" fill="var(--green-bright)"/><circle cx="11" cy="11" r="4" fill="#fff"/></svg>
    <span>5374 Tillbury Fenwood Road<br>Fernhollow, MD 20799</span>
  </address>
</div>
</body>
</html>
```